Shopping centre customer engagement software website

We need a multi page site with :

*What we do.
*How it works.
*Benefits
* Case study
* Testimonial
* Business login (we provide link to business portal)
* Consumer login (we provide link to consumer site)
* Book a demo
* Contact us

We want it to be clean and crisp and very self explanatory with little clutter. We are thinking white but are open to what ever looks the best.
Updates

Wordpress is preferred

Target Market(s)

Shopping centre managers and retail property companies

Coding

Coded - Design and coding required

Number of Pages Required

5+ page

Font styles to use
Sans Serif

Colors
ffffff

Requirements
Must have
• As listed above and must be responsive! Checkout our existing site for the text to be included (will be edited but it’ll give you an idea) www.tovrendix.com

```html
<!DOCTYPE html>
<html lang="en">
<head>
<meta charset="utf-8">
<title>Tovrendix – Shopping Centre Customer Engagement</title>
<link rel="stylesheet" href="https://fonts.googleapis.com/css2?family=PT+Sans:wght@400;700&family=Open+Sans:wght@400;600&display=swap">
<style>
:root{
  --white:#ffffff;
  --ink:#2b2b2b;
  --text:#555555;
  --muted:#8a8a8a;
  --teal:#6cc3d6;
  --teal-deep:#4aaec4;
  --hero-a:#8fd2e2;
  --hero-b:#5fb7cf;
  --hero-ink:#1f2f3a;
  --blue:#2f86d6;
  --blue-light:#4d9fe3;
  --rule:#e6e6e6;
  --footer:#f3f3f3;
}
*{box-sizing:border-box;margin:0;padding:0}
html,body{width:1200px;height:3571px;overflow:hidden}
body{position:relative;background:var(--white);font-family:"Open Sans",Arial,sans-serif;color:var(--text)}
.abs{position:absolute}
h1,h2,h3,h4{font-family:"PT Sans",Arial,sans-serif;color:var(--ink)}

/* header */
.site-header{left:0;top:0;width:1200px;height:107px;background:var(--white)}
.brand{left:106px;top:14px;display:flex;align-items:center;gap:12px}
.brand-dot{width:46px;height:46px;border-radius:50%;background:#9aa3aa}
.brand-name{font-family:"PT Sans",sans-serif;font-size:22px;font-weight:700;color:#555}
.social{top:21px;display:flex;gap:18px;left:842px}
.social span{width:30px;height:30px;border-radius:50%;border:2px solid var(--teal);display:block}
.btn-touch{left:990px;top:23px;width:110px;height:30px;background:var(--teal);color:var(--white);font-size:12px;font-weight:600;text-align:center;line-height:30px}
.main-nav{top:72px;right:98px;display:flex;gap:22px;font-size:14px;color:#333}
.main-nav .active{color:var(--teal)}

/* hero */
.hero{left:0;top:107px;width:1200px;height:448px;background:linear-gradient(135deg,var(--hero-a),var(--hero-b))}
.hero-title{left:0;width:1200px;top:200px;text-align:center;font-family:"PT Sans",sans-serif;font-weight:700;font-size:96px;line-height:110px;color:var(--hero-ink)}
.hero-sub{left:0;width:1200px;top:368px;text-align:center;font-family:"PT Sans",sans-serif;font-weight:700;font-size:20px;line-height:32px;color:var(--hero-ink)}
.hero-dots{left:535px;top:502px;display:flex;gap:8px}
.hero-dots span{width:38px;height:3px;background:rgba(255,255,255,.6)}
.hero-dots span.on{background:var(--hero-ink)}

/* what we do */
.about-photo{left:98px;top:652px;width:476px;height:293px;background:linear-gradient(135deg,#c8bfb4,#7b8391)}
.about-title{left:607px;top:648px;font-size:30px;font-weight:700}
.about-copy{left:612px;top:698px;width:490px;font-size:12px;line-height:21px}
.about-copy p+p{margin-top:12px}
.btn-more{left:612px;top:905px;width:121px;height:40px;background:var(--teal);color:var(--white);font-family:"PT Sans",sans-serif;font-weight:700;font-size:15px;text-align:center;line-height:40px}

/* city band */
.city{left:0;top:1036px;width:1200px;height:364px;background:linear-gradient(180deg,#9ba3ab,#5d6670 70%,#3d444c)}
.city-text{left:0;width:1200px;top:1135px;text-align:center;font-family:"PT Sans",sans-serif;font-weight:700;font-size:26px;line-height:32px;color:var(--white)}
.play{left:570px;top:1258px}

/* benefits */
.benefits-title{left:0;width:1200px;top:1486px;text-align:center;font-size:30px;font-weight:700}
.benefit{top:1568px;width:240px;text-align:center}
.benefit .ring{margin:0 auto;width:178px;height:178px;border-radius:50%;border:11px solid var(--teal);padding:8px}
.benefit .ring div{width:100%;height:100%;border-radius:50%;background:#f6efe6}
.benefit p{margin-top:10px;font-size:12px;line-height:22px;color:#444}
.arrow{top:1640px}

/* mission band */
.mission{left:0;top:1905px;width:1200px;height:428px;background:radial-gradient(circle at 50% 55%,var(--blue-light),var(--blue) 70%)}
.mission-title{left:0;width:1200px;top:1995px;text-align:center;font-size:30px;font-weight:700;line-height:40px;color:var(--white)}
.mission-rule{left:274px;top:2109px;width:655px;height:2px;background:rgba(255,255,255,.55)}
.mission-dot{left:584px;top:2093px;width:34px;height:34px;border-radius:50%;background:#7dc0ec}
.mission-sub{left:0;width:1200px;top:2142px;text-align:center;font-size:30px;font-weight:700;color:var(--white)}
.mission-copy{left:0;width:1200px;top:2188px;text-align:center;font-size:15px;line-height:24px;color:#e3efff}
.chev{left:588px;top:2288px}

/* how it works */
.how-title{left:0;width:1200px;top:2420px;text-align:center;font-size:30px;font-weight:700}
.timeline{left:148px;top:2532px;width:876px;height:12px;background:#111}
.step{top:2515px;width:140px;text-align:center}
.step .num{margin:0 auto;width:44px;height:44px;border-radius:50%;background:var(--white);border:5px solid #111;font-family:"PT Sans",sans-serif;font-weight:700;font-size:14px;line-height:34px;color:#111}
.step.on .num{border-color:var(--teal);color:var(--teal-deep)}
.step p{margin-top:10px;font-family:"PT Sans",sans-serif;font-weight:700;font-size:14px;color:#111}
.step-art{left:357px;top:2600px;width:120px;height:120px;border-radius:50%;background:var(--teal)}

/* contact */
.mall{left:0;top:2822px;width:1200px;height:464px;background:linear-gradient(180deg,#1d2a66,#2e4a8e 55%,#6f86b0)}
.contact-box{left:274px;top:2910px;width:655px;height:345px;background:var(--blue)}
.contact-title{left:274px;width:655px;top:2934px;text-align:center;font-size:30px;font-weight:700;color:var(--white)}
.field{border-bottom:1px solid rgba(255,255,255,.7);color:var(--white);font-size:13px;display:flex;align-items:center;gap:10px;padding-bottom:6px}
.btn-send{left:519px;top:3114px;width:150px;height:46px;border:1px solid var(--white);color:var(--white);font-family:"PT Sans",sans-serif;font-weight:700;font-size:15px;text-align:center;line-height:44px}

/* footer */
.footer{left:0;top:3286px;width:1200px;height:233px;background:var(--footer)}
.footer-fade{left:520px;top:3286px;width:560px;height:233px;background:radial-gradient(ellipse at 60% 50%,#eadfd6,rgba(243,243,243,0) 70%)}
.office{top:3344px;width:240px;font-size:12px;line-height:22px;color:#555}
.office h4{font-size:17px;margin-bottom:14px}
.office .row{display:flex;gap:10px}
.office .row svg{flex:none;margin-top:5px}
.office .ind{padding-left:20px}
.copyright{left:0;top:3519px;width:1200px;height:52px;border-top:1px solid var(--rule);text-align:center;font-size:12px;line-height:52px;color:#666}
</style>
</head>
<body>

<header class="abs site-header">
  <div class="abs brand"><span class="brand-dot"></span><span class="brand-name">Tovrendix</span></div>
  <div class="abs social" aria-label="Social links"><span></span><span></span><span></span></div>
  <a class="abs btn-touch">Get In Touch</a>
  <nav class="abs main-nav">
    <span class="active">Home</span><span>What we do</span><span>Benefits</span><span>Testimonials</span><span>How it works</span><span>Case study</span><span>Contact</span>
  </nav>
</header>

<section>
  <div class="abs hero" role="img" aria-label="Blue tinted photo of a modern shopping centre interior"></div>
  <h1 class="abs hero-title">Tovrendix</h1>
  <p class="abs hero-sub">Tovrendix exceeds all expectations for Shopping Centre<br>Managers, Shoppers, Tenants and Landlords</p>
  <div class="abs hero-dots"><span class="on"></span><span></span><span></span></div>
</section>

<section>
  <div class="abs about-photo" role="img" aria-label="Team working together over documents on a table"></div>
  <h2 class="abs about-title">What we can do for you</h2>
  <div class="abs about-copy">
    <p>Tovrendix provides shopping centre managers with an easy to use platform which enables them to delight their shoppers, impress their tenants, provide detailed data to their landlords and all accessible to them at the click of button.</p>
    <p>Tovrendix gives shopping centres real time tracking through smart ID's of individual customer journeys through their physical stores, enabling highly targeted, relevant and timely promotional and rewarding capabilities. Furthermore, through deep analytical data processing of the customer journey, centre managers will be able to more accurately and reliably predict shopping behaviours.</p>
  </div>
  <a class="abs btn-more">Read More</a>
</section>

<section>
  <div class="abs city" role="img" aria-label="Grey city skyline photo with cranes and towers"></div>
  <p class="abs city-text">Understanding your customers and identifying trends are key to a successful<br>shopping centre, with our innovative and effective services<br>Tovrendix can help you lead the way.</p>
  <svg class="abs play" width="60" height="60" viewBox="0 0 60 60"><circle cx="30" cy="30" r="24" fill="#fff"/><path d="M25 19 L40 30 L25 41 Z" fill="#3d444c"/></svg>
</section>

<section>
  <h2 class="abs benefits-title">Tovrendix Benefits</h2>
  <svg class="abs arrow" style="left:40px" width="16" height="20" viewBox="0 0 16 20"><path d="M11 3 L4 10 L11 17" stroke="#6cc3d6" stroke-width="2" fill="none"/></svg>
  <svg class="abs arrow" style="left:1148px" width="16" height="20" viewBox="0 0 16 20"><path d="M5 3 L12 10 L5 17" stroke="#6cc3d6" stroke-width="2" fill="none"/></svg>
  <div class="abs benefit" style="left:101px"><div class="ring"><div role="img" aria-label="Icon of hands in a handshake"></div></div><p>Increase and measure customer loyalty<br>through tailored targeted rewards and<br>analytics.</p></div>
  <div class="abs benefit" style="left:359px"><div class="ring"><div role="img" aria-label="Icon of a download badge"></div></div><p>Easy to install, no wiring required.</p></div>
  <div class="abs benefit" style="left:620px"><div class="ring"><div role="img" aria-label="Icon of a head with a light bulb"></div></div><p>Know who your customers are personally<br>and when they visit you.</p></div>
  <div class="abs benefit" style="left:882px"><div class="ring"><div role="img" aria-label="Icon of stacked data storage"></div></div><p>Have the data to back up any decision's<br>you make.</p></div>
</section>

<section>
  <div class="abs mission"></div>
  <h2 class="abs mission-title">Tovrendix exists to enable you to understand<br>your customers better!</h2>
  <div class="abs mission-rule"></div>
  <div class="abs mission-dot"></div>
  <h3 class="abs mission-sub">Converged In One Point</h3>
  <p class="abs mission-copy">Tovrendix is the ultimate marketing machine that can help you tailor to each individual and<br>give you insights to do much more for your customers.</p>
  <svg class="abs chev" width="24" height="24" viewBox="0 0 24 24"><path d="M5 5 L12 12 L19 5 M5 12 L12 19 L19 12" stroke="#fff" stroke-width="2" fill="none"/></svg>
</section>

<section>
  <h2 class="abs how-title">How It Works</h2>
  <div class="abs timeline"></div>
  <div class="abs step" style="left:156px"><div class="num">01</div><p>Allocate Cards</p></div>
  <div class="abs step on" style="left:347px"><div class="num">02</div><p>Direct Marketing</p></div>
  <div class="abs step" style="left:537px"><div class="num">03</div><p>Rewarding Loyalty</p></div>
  <div class="abs step" style="left:728px"><div class="num">04</div><p>Collect Data</p></div>
  <div class="abs step" style="left:918px"><div class="num">05</div><p>Data Analytics</p></div>
  <div class="abs step-art" role="img" aria-label="Illustration of direct marketing messages reaching a shopper"></div>
</section>

<section>
  <div class="abs mall" role="img" aria-label="Evening photo of a shopping centre interior with lights"></div>
  <div class="abs contact-box"></div>
  <h2 class="abs contact-title">Contact Us</h2>
  <div class="abs field" style="left:352px;top:3004px;width:225px">
    <svg width="12" height="12" viewBox="0 0 12 12"><circle cx="6" cy="3.5" r="3" fill="#fff"/><path d="M0 12 Q6 4 12 12 Z" fill="#fff"/></svg>Name</div>
  <div class="abs field" style="left:626px;top:3004px;width:225px">
    <svg width="14" height="10" viewBox="0 0 14 10"><rect width="14" height="10" fill="#fff"/><path d="M0 0 L7 6 L14 0" stroke="#2f86d6" fill="none"/></svg>Email</div>
  <div class="abs field" style="left:352px;top:3056px;width:499px">
    <svg width="12" height="12" viewBox="0 0 12 12"><path d="M1 11 L2 8 L9 1 L11 3 L4 10 Z" fill="#fff"/></svg>Message</div>
  <a class="abs btn-send">Send Message</a>
</section>

<footer>
  <div class="abs footer"></div>
  <div class="abs footer-fade" role="img" aria-label="Faint photo of a smiling customer service agent"></div>
  <div class="abs office" style="left:98px">
    <h4>Head Office</h4>
    <div class="row"><svg width="10" height="12" viewBox="0 0 10 12"><path d="M5 12 C1 7 0 5.5 0 4.5 A5 5 0 0 1 10 4.5 C10 5.5 9 7 5 12 Z" fill="#555"/></svg>Unit 9, Harbour Road,</div>
    <div class="ind">Kestow, KT12 4RW</div>
    <div class="row"><svg width="10" height="8" viewBox="0 0 10 8"><rect width="10" height="8" fill="#555"/></svg>owen@tovrendix.com</div>
  </div>
  <div class="abs office" style="left:357px">
    <h4>Branch Office</h4>
    <div class="row"><svg width="10" height="12" viewBox="0 0 10 12"><path d="M5 12 C1 7 0 5.5 0 4.5 A5 5 0 0 1 10 4.5 C10 5.5 9 7 5 12 Z" fill="#555"/></svg>Foundry, 3rd Floor</div>
    <div class="ind">48 Marlow Lane</div>
    <div class="ind">Eastbury, EB4 7LN</div>
    <div class="row"><svg width="10" height="8" viewBox="0 0 10 8"><rect width="10" height="8" fill="#555"/></svg>nadia@tovrendix.com</div>
  </div>
  <div class="abs office" style="left:638px">
    <h4>Branch Office</h4>
    <div class="row"><svg width="10" height="12" viewBox="0 0 10 12"><path d="M5 12 C1 7 0 5.5 0 4.5 A5 5 0 0 1 10 4.5 C10 5.5 9 7 5 12 Z" fill="#555"/></svg>2nd Floor, Alder House</div>
    <div class="ind">Quay Street, Kestow</div>
    <div class="row"><svg width="10" height="8" viewBox="0 0 10 8"><rect width="10" height="8" fill="#555"/></svg>liam@tovrendix.com</div>
  </div>
  <div class="abs office" style="left:919px">
    <h4>Contact Us</h4>
    <div>Our team is always standing by.</div>
    <div>Give us a call!</div>
    <div class="row"><svg width="10" height="12" viewBox="0 0 10 12"><rect x="1" width="8" height="12" rx="1.5" fill="#555"/></svg>Phone | 01632 960418</div>
    <div class="row"><svg width="10" height="8" viewBox="0 0 10 8"><rect width="10" height="8" fill="#555"/></svg>Email | hello@tovrendix.com</div>
  </div>
  <div class="abs copyright">Tovrendix.com © 2018 All rights reserved. Privacy policy</div>
</footer>

</body>
</html>
```